Business Cards Needed for Innovative Healthcare Marketing Company

We are a marketing company focused on healthcare. Our company is all about rebranding yourself renewing your image and generating results. The phoenix stands for "reborn" or "rising" which we provide new brands for our clients we take their old brands and renew it with creativity and innovation. I am looking for a business card with color dimension. I have attached an example of a card I think has the look and feel of what I am trying to accomplish. I like that the card example has black and grey font colors, I like the font placement and the small logo, I really like the use of the colors on the right those are the colors of my logo. My logo is phoenix so maybe incorporating flames similar to that design. I would like the back a solid color maybe red with an opaque version of the logo and website. As a marketing company I am always open to creative liberty!

Target Market(s)

Doctors and business professionals.

Industry/Entity Type

Marketing

Contact Information for Business Card

Vornaly Health Care Marketing
Marnie Okonski- CEO
#(502)638-2947
email-marnie@vornaly.com
website- vornaly.com

Font styles to use
Sans Serif

Colors
ec1f27
f37122
ffc214
fbed22
fbf289
f04a50

Requirements
Must have
• The logo and required information
Nice to have
• icons by the information
Should not have
• child like font

```html
<!DOCTYPE html>
<html lang="en">
<head>
<meta charset="utf-8">
<title>Vornaly Health Care Marketing – Business Card</title>
<link href="https://fonts.googleapis.com/css2?family=Open+Sans:wght@400;600&display=swap" rel="stylesheet">
<style>
  :root {
    --page-bg: #e9e9e7;
    --card-bg: #fbfbfa;
    --card-edge: #d6d6d3;
    --brand-red: #8e1f1c;
    --ink: #2c2c2c;
    --ink-soft: #555555;
    --rule: #9a9a9a;
    --flame-orange: #f37122;
    --flame-deep: #d9531b;
    --ember: #9b1d1b;
    --white: #ffffff;
  }
  * { margin: 0; padding: 0; box-sizing: border-box; }
  html, body {
    width: 1200px;
    height: 970px;
    overflow: hidden;
    background: var(--page-bg);
    font-family: "Open Sans", Arial, sans-serif;
  }
  .card {
    position: absolute;
    left: 100px;
    top: 208px;
    width: 1000px;
    height: 554px;
    border-radius: 28px;
    background: var(--card-bg);
    border: 1px solid var(--card-edge);
    overflow: hidden;
    box-shadow: 0 18px 40px rgba(0,0,0,0.12);
  }
  .brand {
    position: absolute;
    left: 485px;
    top: 78px;
    width: 468px;
    display: flex;
    align-items: center;
    gap: 18px;
  }
  .brand-dot {
    flex: none;
    width: 74px;
    height: 74px;
    border-radius: 50%;
    background: var(--flame-orange);
  }
  .brand-name {
    color: var(--brand-red);
    font-weight: 400;
    font-size: 31px;
    line-height: 1.15;
    letter-spacing: 1px;
    text-transform: uppercase;
  }
  .person-name {
    position: absolute;
    left: 48px;
    top: 248px;
    color: var(--brand-red);
    font-weight: 600;
    font-size: 29px;
    letter-spacing: 0.5px;
    text-transform: uppercase;
  }
  .person-title {
    position: absolute;
    left: 48px;
    top: 286px;
    color: var(--ink-soft);
    font-size: 22px;
  }
  .divider {
    position: absolute;
    left: 48px;
    top: 332px;
    width: 680px;
    height: 1.5px;
    background: var(--rule);
  }
  .address {
    position: absolute;
    left: 48px;
    top: 348px;
    color: var(--ink-soft);
    font-size: 23px;
    line-height: 33px;
    font-style: normal;
  }
  .contact {
    position: absolute;
    right: 46px;
    top: 315px;
    list-style: none;
    text-align: right;
    color: var(--ink);
    font-size: 22px;
    line-height: 37px;
  }
  .contact li { display: flex; justify-content: flex-end; align-items: center; gap: 8px; }
  .contact svg { width: 22px; height: 18px; fill: var(--brand-red); }
  .wave { position: absolute; left: 0; top: 0; }
  .website {
    position: absolute;
    right: 46px;
    top: 486px;
    color: var(--white);
    font-size: 22px;
    letter-spacing: 1px;
  }
</style>
</head>
<body>
  <section class="card">
    <svg class="wave" width="1000" height="554" viewBox="0 0 1000 554" aria-hidden="true">
      <defs>
        <linearGradient id="flameBand" x1="0" y1="0" x2="1" y2="0">
          <stop offset="0" stop-color="var(--flame-orange)"/>
          <stop offset="0.55" stop-color="var(--flame-deep)"/>
          <stop offset="1" stop-color="var(--ember)"/>
        </linearGradient>
      </defs>
      <path d="M0 486 C200 506 400 506 560 476 C700 450 850 440 1000 446 L1000 554 L0 554 Z" fill="url(#flameBand)"/>
      <path d="M0 448 C150 470 380 486 600 462 C380 480 150 478 0 468 Z" fill="var(--ember)"/>
    </svg>

    <div class="brand">
      <span class="brand-dot"></span>
      <span class="brand-name">Vornaly<br>Health Care Marketing</span>
    </div>

    <h1 class="person-name">Marnie Okonski</h1>
    <p class="person-title">CEO</p>
    <div class="divider"></div>

    <address class="address">
      Level 14, 8 Harlow Tower<br>
      Carlow, 20, New Bramwell
    </address>

    <ul class="contact">
      <li>(502)638-2947
        <svg viewBox="0 0 24 20"><path d="M2 7 C2 3 7 2 12 2 C17 2 22 3 22 7 L18 8 L17 5 C14 4 10 4 7 5 L6 8 Z M5 10 L9 6 L15 6 L19 10 L19 18 L5 18 Z"/></svg>
      </li>
      <li>marnie@vornaly.com
        <svg viewBox="0 0 24 18"><path d="M1 2 H23 V16 H1 Z M3 4 V5 L12 11 L21 5 V4 Z" fill-rule="evenodd"/></svg>
      </li>
    </ul>

    <p class="website">www.vornaly.com</p>
  </section>
</body>
</html>
```